Infographics breakdown for small group

An infographic is needed to display the different personality types from a spreadsheet for 18 individuals. Name of the organization: Riverstone Harvest Fellowship Atlanta

Infographics of an Excel spreadsheet for 19 people at a church. The name of the church is Riverstone Harvest Fellowhsip Atlanta.

Target Market(s)

Church group

Industry/Entity Type

Spirtual

Requirements
Must have
• Age, Personality, and Spiritual Gifts breakdown
Nice to have
• Compelling photo,
Should not have
• I'm okay with the designer deciding

```html
<!DOCTYPE html>
<html lang="en">
<head>
<meta charset="utf-8">
<title>Personality Type &amp; Top 5 Gifts – Riverstone Harvest Fellowship Atlanta</title>
<link href="https://fonts.googleapis.com/css2?family=Roboto+Slab:wght@400;700;800&family=Arimo:wght@400;700&display=swap" rel="stylesheet">
<style>
  :root {
    --ink: #1e1e1e;
    --band: #1f1f1f;
    --paper-top: #fde6d6;
    --paper-bottom: #fdf4ec;
    --tag: #f9d4bb;
    --rule: #2a2a2a;
    --white: #ffffff;
  }
  html, body { margin: 0; padding: 0; overflow: hidden; }
  body { width: 848px; height: 1200px; }
  .poster {
    position: relative;
    width: 848px;
    height: 1200px;
    overflow: hidden;
    background: linear-gradient(180deg, var(--paper-top) 0%, var(--paper-bottom) 100%);
    color: var(--ink);
    font-family: "Arimo", Arial, sans-serif;
  }
  .masthead {
    position: absolute; left: 0; top: 0; width: 848px; height: 140px;
    background: var(--band);
  }
  .masthead__title {
    position: absolute; left: 50px; top: 38px; margin: 0;
    font-family: "Roboto Slab", serif; font-weight: 800;
    font-size: 29px; line-height: 35px; color: var(--white); letter-spacing: -0.3px;
  }
  .org {
    position: absolute; left: 474px; top: 36px; display: flex; align-items: center; gap: 12px;
  }
  .org__dot { width: 58px; height: 58px; border: 3px solid var(--white); border-radius: 50%; box-sizing: border-box; }
  .org__name { font-family: "Roboto Slab", serif; font-weight: 700; color: var(--white); font-size: 22px; line-height: 27px; }
  .org__sub { font-family: "Arimo", Arial, sans-serif; color: var(--white); font-size: 17px; line-height: 20px; display: block; }

  .group { position: absolute; left: 0; width: 848px; }
  .group__label { position: absolute; left: 50px; top: 0; width: 170px; }
  .group__name {
    margin: 0; font-family: "Roboto Slab", serif; font-weight: 700;
    font-size: 19px; line-height: 22px; letter-spacing: 1.2px;
  }
  .group__code { margin: 8px 0 6px; font-weight: 700; font-size: 13px; line-height: 15px; }
  .group__desc { margin: 0; font-size: 10.5px; line-height: 13.6px; }
  .group__divider { position: absolute; left: 235px; top: -8px; width: 1px; background: var(--rule); }
  .rule { position: absolute; left: 48px; width: 754px; height: 1px; background: var(--rule); }

  .member { position: absolute; width: 150px; }
  .member__name {
    display: inline-block; background: var(--tag); padding: 2px 5px 3px 8px; margin-left: -8px;
    font-family: "Roboto Slab", serif; font-weight: 700; font-size: 13.6px; line-height: 15px; white-space: nowrap;
  }
  .member__gifts { margin: 8px 0 0; padding: 0; list-style: none; font-size: 12.4px; line-height: 15.6px; }

  .footer {
    position: absolute; left: 0; top: 1170px; width: 848px; height: 30px; background: var(--band);
  }
  .footer__handle {
    position: absolute; right: 14px; top: 6px; color: var(--white);
    font-family: "Roboto Slab", serif; font-size: 14px;
  }
</style>
</head>
<body>
<main class="poster">
  <header class="masthead">
    <h1 class="masthead__title">PERSONALITY TYPE &amp;<br>TOP 5 GIFTS</h1>
    <div class="org">
      <div class="org__dot"></div>
      <div class="org__name">Riverstone Harvest<span class="org__sub">Fellowhsip Atlanta</span></div>
    </div>
  </header>

  <!-- Commander -->
  <section class="group" style="top:158px;">
    <div class="group__label">
      <h2 class="group__name">COMMANDER</h2>
      <p class="group__code">ENTJ-A/ENTJ-T</p>
      <p class="group__desc">(Bold, imaginative and strong-willed leaders, always finding a way- or making one.)</p>
    </div>
    <div class="group__divider" style="height:242px;"></div>
    <div class="member" style="left:268px;top:0;"><span class="member__name">Marcus Whitfield</span><ul class="member__gifts"><li>Administration,</li><li>Apostleship,</li><li>Craftsmanship,</li><li>Discernment,</li><li>Evangelism</li></ul></div>
    <div class="member" style="left:418px;top:0;"><span class="member__name">Loretta-Mae Quinn</span><ul class="member__gifts"><li>Faith,</li><li>Giving,</li><li>Leadership,</li><li>Miracles,</li><li>Teaching</li></ul></div>
    <div class="member" style="left:571px;top:0;"><span class="member__name">Denise Hale</span><ul class="member__gifts"><li>Apostleship,</li><li>Craftsmanship,</li><li>Exhortation,</li><li>Faith,</li><li>Giving</li></ul></div>
    <div class="member" style="left:694px;top:0;"><span class="member__name">Tamika Ruiz</span><ul class="member__gifts"><li>Administration,</li><li>Faith,</li><li>Healing,</li><li>Mercy,</li><li>Teaching</li></ul></div>
    <div class="member" style="left:268px;top:128px;"><span class="member__name">Gregory Ashworth</span><ul class="member__gifts"><li>Administration,</li><li>Discernment,</li><li>Evangelism,</li><li>Pastor/Shepherd,</li><li>Prophecy</li></ul></div>
    <div class="member" style="left:418px;top:128px;"><span class="member__name">Janet Brooks</span><ul class="member__gifts"><li>Evangelism,</li><li>Word of Knowledge,</li><li>Mercy,</li><li>Miracles,</li><li>Teaching</li></ul></div>
    <div class="member" style="left:571px;top:128px;"><span class="member__name">Shanelle Voss</span><ul class="member__gifts"><li>Exhortation,</li><li>Word of Knowledge,</li><li>Admistration,</li><li>Teaching,</li><li>Prophecy</li></ul></div>
  </section>
  <div class="rule" style="top:410px;"></div>

  <!-- Protagonist -->
  <section class="group" style="top:436px;">
    <div class="group__label">
      <h2 class="group__name">PROTAGONIST</h2>
      <p class="group__code">ENFJ-A/ENFJ-T</p>
      <p class="group__desc">(Charismatic and inspiring leaders, able to mesmerize their listeners.)</p>
    </div>
    <div class="group__divider" style="height:116px;"></div>
    <div class="member" style="left:268px;top:0;"><span class="member__name">Nathan Pryor</span><ul class="member__gifts" style="margin-top:5px;"><li>Apostleship,</li><li>Discernment,</li><li>Evangelism,</li><li>Faith,</li><li>Giving</li></ul></div>
    <div class="member" style="left:418px;top:0;"><span class="member__name">Lydia Holloway</span><ul class="member__gifts" style="margin-top:5px;"><li>Apostleship,</li><li>Discernment,</li><li>Evangelism,</li><li>Faith,</li><li>Words of Wisdom</li></ul></div>
    <div class="member" style="left:571px;top:0;"><span class="member__name">Bernice Tate</span><ul class="member__gifts" style="margin-top:5px;"><li>Evangelism</li><li>Exhortation,</li><li>Faith,</li><li>Healing,</li><li>Teaching</li></ul></div>
    <div class="member" style="left:694px;top:0;"><span class="member__name">Clarence Tate</span><ul class="member__gifts" style="margin-top:5px;"><li>Craftsmanship,</li><li>Evangelism,</li><li>Faith,</li><li>Healing,</li><li>Teaching</li></ul></div>
  </section>
  <div class="rule" style="top:564px;"></div>

  <!-- Adventurer -->
  <section class="group" style="top:593px;">
    <div class="group__label">
      <h2 class="group__name">ADVENTURER</h2>
      <p class="group__code" style="margin:6px 0 3px;">ISFP-A/ISFP-T</p>
      <p class="group__desc">(Flexible and charming artists, always ready to explore and experience something new.)</p>
    </div>
    <div class="group__divider" style="height:112px;"></div>
    <div class="member" style="left:268px;top:0;"><span class="member__name">Rosalyn Holloway</span><ul class="member__gifts" style="margin-top:5px;"><li>Craftsmanship,</li><li>Exhortation,</li><li>Helps,</li><li>Mercy,</li><li>Service</li></ul></div>
  </section>
  <div class="rule" style="top:718px;"></div>

  <!-- Executive -->
  <section class="group" style="top:743px;">
    <div class="group__label">
      <h2 class="group__name">EXECUTIVE</h2>
      <p class="group__code" style="margin:10px 0 10px;">ESTJ-A/ESTJ-T</p>
      <p class="group__desc">(Excellent administrators, unsurpassed at managing things or people.)</p>
    </div>
    <div class="group__divider" style="height:114px;"></div>
    <div class="member" style="left:268px;top:0;"><span class="member__name">Everett Holloway</span><ul class="member__gifts" style="margin-top:7px;"><li>Craftsmanship,</li><li>Exhortation,</li><li>Faith,</li><li>Helps,</li><li>Leadership</li></ul></div>
    <div class="member" style="left:418px;top:0;"><span class="member__name">Derek Lawson</span><ul class="member__gifts" style="margin-top:7px;"><li>Craftsmanship,</li><li>Giving,</li><li>Healing,</li><li>Miracles,</li><li>Teaching</li></ul></div>
  </section>
  <div class="rule" style="top:872px;"></div>

  <!-- Entrepreneur -->
  <section class="group" style="top:898px;">
    <div class="group__label">
      <h2 class="group__name">ENTREPRENEUR</h2>
      <p class="group__code" style="margin:6px 0 10px;">ESTP-A/ESTP-T</p>
      <p class="group__desc">(Smart, energetic and very perceptive people, who truly enjoy living on the edge.)</p>
    </div>
    <div class="group__divider" style="height:112px;"></div>
    <div class="member" style="left:268px;top:0;"><span class="member__name">Walter Prescott Jr</span><ul class="member__gifts" style="margin-top:5px;"><li>Apostleship,</li><li>Exhortation,</li><li>Faith,</li><li>Giving,</li><li>Teaching</li></ul></div>
    <div class="member" style="left:418px;top:0;"><span class="member__name">Monica Lawson</span><ul class="member__gifts" style="margin-top:5px;"><li>Exhortation,</li><li>Giving,</li><li>Mercy,</li><li>Miracles,</li><li>Prophecy</li></ul></div>
  </section>
  <div class="rule" style="top:1026px;"></div>

  <!-- Architect -->
  <section class="group" style="top:1048px;">
    <div class="group__label">
      <h2 class="group__name">ARCHITECT</h2>
      <p class="group__code" style="margin:8px 0 8px;">INTJ-A/INTJ-T</p>
      <p class="group__desc">(Imaginative and strategic thinkers, with<br>a plan for everything.)</p>
    </div>
    <div class="group__divider" style="height:116px;"></div>
    <div class="member" style="left:268px;top:0;"><span class="member__name">Gloria Prescott</span><ul class="member__gifts" style="margin-top:7px;"><li>Administration,</li><li>Apostleship,</li><li>Craftsmanship,</li><li>Discernment,</li><li>Helps</li></ul></div>
    <div class="member" style="left:418px;top:0;"><span class="member__name">Adrienne Finch</span><ul class="member__gifts" style="margin-top:7px;"><li>Administration,</li><li>Discernment,</li><li>Exhortation,</li><li>Prophecy,</li><li>Teaching</li></ul></div>
  </section>

  <footer class="footer">
    <span class="footer__handle">@RiverstoneHarvest</span>
  </footer>
</main>
</body>
</html>
```